CBD PATCHES

Design creation of my CBD patch box.
Product must look Pharamaceutical grade.
Colours need to look pharmaceutical (green/white/maybe a bit of blue).
Text: Cannabidiol (CBD) Self-curing adhesive Polyethylene backing sheet.
Apply one patch to a smooth are of skin. Each patch can be worn for up to 24 hours. Apply subsequent patches to different areas to allow the skin to breathe between uses.
Do not apply to broken or irritable skin. Consult a doctor if you are taking medications or have medical conditions before using this or any other supplement. Do not use if you are pregnant or breastfeeding.
Store in a cool, dry place out of direct sunlight. Stable for three years. Once opened, use within 12 months.

```html
<!DOCTYPE html>
<html lang="en">
<head>
<meta charset="utf-8">
<title>Verdacare CBD Patches – Box Front and Dielines</title>
<link rel="stylesheet" href="https://fonts.googleapis.com/css2?family=Outfit:wght@400;600;700;800&family=Comfortaa:wght@600&display=swap">
<style>
  :root {
    --paper: #ffffff;
    --mint: #ccffaa;
    --leaf: #9ed97b;
    --ink: #1a1a1a;
    --rule: #a8c2b6;
  }
  html, body {
    margin: 0;
    padding: 0;
    overflow: hidden;
    background: var(--paper);
  }
  .canvas {
    position: relative;
    width: 1200px;
    height: 849px;
    background: var(--paper);
    overflow: hidden;
    font-family: "Outfit", sans-serif;
  }
  .artwork {
    position: absolute;
    inset: 0;
  }
  .brand-name {
    font-family: "Outfit", sans-serif;
    font-weight: 800;
    fill: var(--mint);
  }
  .sub-name {
    font-family: "Outfit", sans-serif;
    font-weight: 800;
    fill: var(--mint);
  }
  .strength {
    font-family: "Comfortaa", sans-serif;
    font-weight: 600;
    fill: var(--paper);
  }
  .claims {
    font-family: "Outfit", sans-serif;
    font-weight: 700;
    fill: var(--ink);
  }
  .dieline {
    fill: none;
    stroke: var(--rule);
    stroke-width: 0.8;
  }
  .info-panel {
    position: absolute;
    left: 631px;
    top: 394px;
    width: 146px;
    color: var(--ink);
    font-size: 5.5px;
    line-height: 7px;
    font-weight: 600;
  }
  .info-panel h3 {
    margin: 0;
    font-size: 5.8px;
    font-weight: 800;
    letter-spacing: 0.1px;
  }
  .info-panel p {
    margin: 0 0 6px;
  }
  .produced-by {
    position: absolute;
    left: 1018px;
    top: 560px;
    font-size: 6.5px;
    font-weight: 700;
    color: var(--ink);
    margin: 0;
  }
</style>
</head>
<body>
<div class="canvas">
  <svg class="artwork" width="1200" height="849" viewBox="0 0 1200 849" xmlns="http://www.w3.org/2000/svg">
    <!-- Front panel -->
    <g class="front-panel">
      <rect x="70" y="112" width="442" height="461" fill="var(--paper)"/>
      <circle cx="291" cy="238" r="105" fill="var(--mint)"/>
      <text class="brand-name" x="291" y="396" font-size="36" text-anchor="middle" letter-spacing="1">VERDACARE</text>
      <text class="sub-name" x="291" y="422" font-size="17" text-anchor="middle" letter-spacing="0.5">CBD PATCHES</text>
      <rect x="70" y="474" width="442" height="99" fill="var(--mint)"/>
      <rect x="136" y="456" width="309" height="42" rx="21" fill="var(--leaf)"/>
      <text class="strength" x="290.5" y="483" font-size="17" text-anchor="middle">20mg CBD isolate per patch</text>
      <text class="claims" x="291" y="534" font-size="17" text-anchor="middle">VEGAN • THC FREE • 100% CANNABIDIOL</text>
    </g>

    <!-- Inside dieline -->
    <g class="dieline-inside">
      <path class="dieline" d="M624 321 H674 A27 27 0 0 1 728 321 H780 V707 H624 Z"/>
      <line class="dieline" x1="624" y1="387" x2="780" y2="387"/>
      <line class="dieline" x1="624" y1="550" x2="780" y2="550"/>
      <path class="dieline" d="M624 556 C590 558 565 590 565 625 V702 H624"/>
      <path class="dieline" d="M780 556 C814 558 838 590 838 625 V702 H780"/>
      <path class="dieline" d="M624 707 C633 710 637 716 637 724 V779 H680 A22 22 0 0 1 724 779 H766 V724 C766 716 771 710 780 707"/>
      <line class="dieline" x1="584" y1="634" x2="610" y2="661"/>
      <line class="dieline" x1="819" y1="634" x2="793" y2="661"/>
      <path class="dieline" d="M670 642 L674 647 H729 L733 642"/>
    </g>

    <!-- Outside dieline -->
    <g class="dieline-outside">
      <path class="dieline" d="M932 321 H982 A27 27 0 0 1 1036 321 H1088 V707 H932 Z"/>
      <rect x="932" y="387" width="156" height="35" fill="var(--mint)"/>
      <line class="dieline" x1="932" y1="550" x2="1088" y2="550"/>
      <path class="dieline" d="M932 556 C898 558 873 590 873 625 V702 H932"/>
      <path class="dieline" d="M1088 556 C1122 558 1146 590 1146 625 V702 H1088"/>
      <path class="dieline" d="M932 707 C941 710 945 716 945 724 V779 H988 A22 22 0 0 1 1032 779 H1074 V724 C1074 716 1079 710 1088 707"/>
      <line class="dieline" x1="892" y1="634" x2="918" y2="661"/>
      <line class="dieline" x1="1127" y1="634" x2="1101" y2="661"/>
      <path class="dieline" d="M978 642 L982 647 H1037 L1041 642"/>

      <g class="top-face-inverted" transform="rotate(180 1010 440)">
        <text class="claims" x="1010" y="476" font-size="6.6" text-anchor="middle">VEGAN • THC FREE • 100% CANNABIDIOL</text>
        <rect x="956" y="452" width="108" height="14" rx="7" fill="var(--leaf)"/>
        <text class="strength" x="1010" y="462" font-size="6.2" text-anchor="middle">20mg CBD isolate per patch</text>
        <text class="sub-name" x="1010" y="440" font-size="5.5" text-anchor="middle">CBD PATCHES</text>
        <text class="brand-name" x="1010" y="432" font-size="12" text-anchor="middle">VERDACARE</text>
        <circle cx="1011" cy="376" r="37" fill="var(--mint)"/>
      </g>
    </g>
  </svg>

  <div class="info-panel">
    <h3>INGREDIENTS</h3>
    <p>Cannabidiol (CBD) Self-curing adhesive Polyethylene backing sheet.</p>
    <h3>DIRECTIONS</h3>
    <p>Apply one patch to a smooth are of skin. Each patch can be worn for up to 24 hours. Apply subsequent patches to different areas to allow the skin to breathe between uses.</p>
    <h3>ADVISOR INFORMATION</h3>
    <p>Do not apply to broken or irritable skin. Consult a doctor if you are taking medications or have medical conditions before using this or any other supplement. Do not use if you are pregnant or breastfeeding.</p>
    <h3>STORAGE</h3>
    <p>Store in a cool, dry place out of direct sunlight. Stable for three years. Once opened, use within 12 months.</p>
  </div>

  <p class="produced-by">PRODUCED BY:</p>
</div>
</body>
</html>
```